Update Business Card Design

I'm looking to update my business cards. Attached is a photo of the current design. I like the black side so that does not have to be update. The white side needs to be updated. I want the design to be modern and minimalistic.
I am a lawyer and my firm's website is www.brennoxlegalco.com (for reference).
My firm's logo has a horizontal version (which is on the black side of the card) and a vertical version (on the white side). I would prefer to keep the vertical version on the white side and horizontal version on the black side (the logo files are attached).

I am open to redesigning the black side also. I would like one side to have the horizontal logo and the other to have the vertical logo.

```html
<!DOCTYPE html>
<html lang="en">
<head>
<meta charset="utf-8">
<title>Brennox Legal Co. – Business Card</title>
<link href="https://fonts.googleapis.com/css2?family=Cinzel:wght@400&family=Lato:wght@400;700;900&display=swap" rel="stylesheet">
<style>
  :root {
    --stage: #3a3a3a;
    --card-light: #ffffff;
    --card-dark: #1c1c1d;
    --brand-blue: #12b5e2;
    --ink: #4a4a4a;
    --ink-soft: #8a8a8a;
    --paper-text: #ffffff;
  }
  * { box-sizing: border-box; margin: 0; padding: 0; }
  html, body {
    width: 1200px; height: 801px; overflow: hidden;
    background: var(--stage);
  }
  .stage {
    position: relative; width: 1200px; height: 801px;
    display: flex; align-items: center; justify-content: center; gap: 60px;
  }
  .card {
    width: 500px; height: 286px; border-radius: 16px;
    position: relative; overflow: hidden;
    border-bottom: 3px solid var(--brand-blue);
    box-shadow: 0 18px 40px rgba(0,0,0,.35);
  }
  /* Front */
  .card--front { background: var(--card-light); display: flex; }
  .front__brand {
    width: 215px; display: flex; flex-direction: column;
    align-items: center; justify-content: center; gap: 12px;
  }
  .brand-mark { width: 18px; height: 18px; background: var(--brand-blue); border-radius: 50%; }
  .brand-name {
    font-family: "Cinzel", serif; font-weight: 400; color: var(--brand-blue);
    text-align: center; line-height: 1.05; font-size: 30px; letter-spacing: 1px;
  }
  .front__divider { width: 1px; background: var(--brand-blue); margin: 58px 0; }
  .front__details { padding: 52px 0 0 26px; }
  .person-name {
    font-family: "Lato", sans-serif; font-weight: 900; color: var(--brand-blue);
    font-size: 22px; letter-spacing: .5px; text-transform: uppercase;
  }
  .person-title {
    font-family: "Lato", sans-serif; color: var(--ink-soft); font-size: 12.5px;
    margin: 2px 0 16px;
  }
  .contact { list-style: none; font-family: "Lato", sans-serif; color: var(--ink); font-size: 12.5px; }
  .contact li { display: flex; align-items: flex-start; gap: 9px; line-height: 1.45; }
  .contact svg { width: 11px; height: 11px; margin-top: 3px; flex: none; fill: var(--brand-blue); }
  .contact .addr { margin-bottom: 2px; }
  /* Back */
  .card--back { background: var(--card-dark); display: flex; align-items: center; justify-content: center; gap: 18px; }
  .back__mark { width: 22px; height: 22px; background: var(--brand-blue); border-radius: 50%; }
  .back__divider { width: 1px; height: 70px; background: var(--paper-text); }
  .back__name {
    font-family: "Cinzel", serif; font-weight: 400; color: var(--paper-text);
    font-size: 40px; line-height: 1.05; letter-spacing: 1px;
  }
</style>
</head>
<body>
<main class="stage">
  <section class="card card--front" aria-label="Card front">
    <div class="front__brand">
      <span class="brand-mark"></span>
      <p class="brand-name">Brennox<br>Legal Co.</p>
    </div>
    <div class="front__divider"></div>
    <div class="front__details">
      <h1 class="person-name">Daniel Okafor</h1>
      <p class="person-title">Attorney at Law</p>
      <ul class="contact">
        <li class="addr"><svg viewBox="0 0 12 12"><path d="M6 0a4 4 0 0 0-4 4c0 3 4 8 4 8s4-5 4-8a4 4 0 0 0-4-4zm0 5.5A1.5 1.5 0 1 1 6 2.5a1.5 1.5 0 0 1 0 3z"/></svg><span>180 W. Harlow Avenue, Suite 310<br>Westbrook, CA 90417</span></li>
        <li><svg viewBox="0 0 12 12"><path d="M2.5 0.5l2 2.5-1 1.2a7 7 0 0 0 4.3 4.3l1.2-1 2.5 2-1.2 2C5 11.5.5 7 .5 1.7z"/></svg><span>555.214.3380</span></li>
        <li><svg viewBox="0 0 12 12"><path d="M3 0h6v12H3zM4 1.5v8h4v-8z"/></svg><span>555.602.7145</span></li>
        <li><svg viewBox="0 0 12 12"><path d="M3 0h6v3H3zM0 4h12v6h-2v2H2v-2H0zm3 4v3h6V8z"/></svg><span>555.214.3391</span></li>
        <li><svg viewBox="0 0 12 12"><path d="M0 2h12v8H0zm1 1v.4l5 3.3 5-3.3V3z"/></svg><span>daniel@brennoxlegalco.com</span></li>
        <li><svg viewBox="0 0 12 12"><path d="M6 0a6 6 0 1 0 0 12A6 6 0 0 0 6 0zm0 1.2c.8 0 1.6 2 1.7 4.2H4.3C4.4 3.2 5.2 1.2 6 1.2zM4.3 6.6h3.4C7.6 8.8 6.8 10.8 6 10.8S4.4 8.8 4.3 6.6z"/></svg><span>www.brennoxlegalco.com</span></li>
      </ul>
    </div>
  </section>

  <section class="card card--back" aria-label="Card back">
    <span class="back__mark"></span>
    <span class="back__divider"></span>
    <p class="back__name">Brennox<br>Legal Co.</p>
  </section>
</main>
</body>
</html>
```